Spino-Tarla
business card/ stationary
Spino-Tarla - Health
Creative Brief
Professional
Dr. Martin Pettigrew
Chiropractic Physician, CHO
914 Halden Rd Solana Beach, CA 92318
mpw@spino-tarla.example
www.spino-tarla.example
use small logo as bullet for back of business card info. line 1 Health - Happiness - Abundance then bullets
Health - Happiness - Abundance - Natural Chiropractic Care: family wellness, chronic pain relief, personal injury - Ayurvedic Consultation: conscious lifestyle programs for stress management, nutrition, weight loss, physical and emotional balance - Quiet Current Stillness Practice: group and private instruction - Wellbeing Educational Seminars

```html
<!DOCTYPE html>
<html lang="en">
<head>
<meta charset="utf-8">
<title>Spino-Tarla Stationery</title>
<link href="https://fonts.googleapis.com/css2?family=Cinzel:wght@600&family=Open+Sans:wght@400;600&display=swap" rel="stylesheet">
<style>
:root{
  --board-light:#4a5a1e;
  --board-dark:#1c250a;
  --leaf:#8cbf2f;
  --leaf-soft:#c9e08a;
  --forest:#2c4410;
  --forest-mid:#4f7a1a;
  --saffron:#e8801f;
  --paper:#ffffff;
  --ink:#4a4a3a;
  --label:#c8d0a8;
}
*{box-sizing:border-box;margin:0;padding:0}
html,body{width:1200px;height:382px;overflow:hidden}
body{
  position:relative;
  background:radial-gradient(ellipse at 40% 30%,var(--board-light),var(--board-dark) 85%);
  font-family:"Open Sans",Arial,sans-serif;color:var(--ink);
}
.brand-mark{position:absolute;left:30px;top:48px;width:120px;text-align:center}
.brand-mark .dot{display:block;width:30px;height:30px;border-radius:50%;background:var(--saffron);margin:0 auto 8px}
.brand-name{font-family:"Cinzel",Georgia,serif;font-weight:600;color:var(--leaf);letter-spacing:.5px}
.brand-mark .brand-name{font-size:15px}
.brand-mark .tagline{font-size:7px;color:var(--label);margin-top:22px}

.card{position:absolute;width:125px;height:86px;padding:7px 8px;font-size:4.6px;line-height:1.45;box-shadow:0 2px 5px rgba(0,0,0,.45)}
.card-back{background:var(--forest);color:#e4edc8}
.card-back.alt{background:linear-gradient(160deg,var(--forest-mid),var(--forest))}
.card-back .motto{font-weight:600;color:var(--leaf-soft);margin-bottom:3px}
.card-back ul{list-style:none}
.card-back li{position:relative;padding-left:6px}
.card-back li::before{content:"";position:absolute;left:0;top:2px;width:3px;height:3px;border-radius:50%;background:var(--saffron)}
.card-back .brand-name{position:absolute;left:8px;bottom:6px;font-size:6px;color:var(--leaf-soft)}
.card-front{background:var(--paper)}
.card-front.alt{background:linear-gradient(180deg,var(--paper) 40%,var(--leaf-soft))}
.card-front .logo-row{display:flex;align-items:center;gap:4px}
.card-front .logo-row i{width:9px;height:9px;border-radius:50%;background:var(--saffron)}
.card-front .brand-name{font-size:8px}
.card-front .person{margin-top:14px;font-weight:600;font-size:5.5px;color:var(--forest)}
.card-front .contact{margin-top:3px}

.label{position:absolute;font-size:5px;color:var(--label);text-align:center}

.letterhead{position:absolute;top:24px;width:150px;height:326px;background:var(--paper);box-shadow:0 3px 8px rgba(0,0,0,.5);padding:18px 14px}
.letterhead .bar{position:absolute;right:0;top:0;width:10px;height:48px;background:var(--leaf)}
.letterhead .head{text-align:center}
.letterhead .head i{display:block;width:16px;height:16px;border-radius:50%;background:var(--saffron);margin:0 auto 3px}
.letterhead .brand-name{font-size:10px}
.letterhead .foot{position:absolute;left:14px;right:14px;bottom:14px;font-size:4px;line-height:1.5;text-align:center;border-top:1px solid var(--leaf-soft);padding-top:4px}

.envelope{position:absolute;left:728px;width:168px;height:76px;box-shadow:0 2px 6px rgba(0,0,0,.45)}
.envelope svg{display:block}
</style>
</head>
<body>

<div class="brand-mark">
  <span class="dot"></span>
  <div class="brand-name">Spino-Tarla</div>
  <div class="tagline">Wellness Concepts</div>
</div>

<!-- row one -->
<div class="card card-back" style="left:19px;top:149px">
  <p class="motto">Health - Happiness - Abundance</p>
  <ul>
    <li>Natural Chiropractic Care: family wellness, chronic pain relief, personal injury</li>
    <li>Ayurvedic Consultation: conscious lifestyle programs</li>
    <li>Quiet Current Stillness Practice</li>
    <li>Wellbeing Educational Seminars</li>
  </ul>
  <span class="brand-name">Spino-Tarla</span>
</div>
<div class="card card-front" style="left:151px;top:149px">
  <div class="logo-row"><i></i><span class="brand-name">Spino-Tarla</span></div>
  <p class="person">Dr. Martin Pettigrew</p>
  <p>Chiropractic Physician, CHO</p>
  <p class="contact">914 Halden Rd Solana Beach, CA 92318<br>mpw@spino-tarla.example<br>www.spino-tarla.example</p>
</div>
<div class="label" style="left:19px;top:240px;width:125px">Business Card Back</div>
<div class="label" style="left:151px;top:240px;width:125px">Business Card Front</div>

<!-- row two -->
<div class="card card-back alt" style="left:19px;top:259px">
  <p class="motto">Health - Happiness - Abundance</p>
  <ul>
    <li>Natural Chiropractic Care: family wellness, chronic pain relief, personal injury</li>
    <li>Ayurvedic Consultation: conscious lifestyle programs</li>
    <li>Quiet Current Stillness Practice</li>
    <li>Wellbeing Educational Seminars</li>
  </ul>
  <span class="brand-name">Spino-Tarla</span>
</div>
<div class="card card-front alt" style="left:151px;top:259px">
  <div class="logo-row"><i></i><span class="brand-name">Spino-Tarla</span></div>
  <p class="person">Dr. Martin Pettigrew</p>
  <p>Chiropractic Physician, CHO</p>
  <p class="contact">914 Halden Rd Solana Beach, CA 92318<br>mpw@spino-tarla.example<br>www.spino-tarla.example</p>
</div>
<div class="label" style="left:19px;top:350px;width:125px">Business Card Back</div>
<div class="label" style="left:151px;top:350px;width:125px">Business Card Front</div>

<!-- letterheads -->
<div class="letterhead" style="left:331px">
  <span class="bar"></span>
  <div class="head"><i></i><span class="brand-name">Spino-Tarla</span></div>
  <div class="foot">Dr. Martin Pettigrew · 914 Halden Rd Solana Beach, CA 92318<br>mpw@spino-tarla.example · www.spino-tarla.example</div>
</div>
<div class="letterhead" style="left:523px">
  <span class="bar"></span>
  <div class="head"><i></i><span class="brand-name">Spino-Tarla</span></div>
  <div class="foot">Dr. Martin Pettigrew · 914 Halden Rd Solana Beach, CA 92318<br>mpw@spino-tarla.example · www.spino-tarla.example</div>
</div>
<div class="label" style="left:331px;top:358px;width:150px">Letterhead Page One</div>
<div class="label" style="left:523px;top:358px;width:150px">Letterhead Page Two</div>

<!-- envelopes, back to front -->
<div class="envelope" style="top:262px">
  <svg width="168" height="76" viewBox="0 0 168 76"><rect width="168" height="76" fill="#fff"/><path d="M0 0 L84 40 L168 0" fill="none" stroke="#dfe6cf"/></svg>
</div>
<div class="envelope" style="top:190px">
  <svg width="168" height="76" viewBox="0 0 168 76"><rect width="168" height="76" fill="#fff"/><path d="M0 0 L84 40 L168 0" fill="none" stroke="#dfe6cf"/><circle cx="16" cy="60" r="4" fill="#e8801f"/><text x="24" y="62" font-family="Cinzel,serif" font-size="6" fill="#8cbf2f">Spino-Tarla</text></svg>
</div>
<div class="envelope" style="top:100px">
  <svg width="168" height="76" viewBox="0 0 168 76"><defs><linearGradient id="flapGreen" x1="0" y1="0" x2="0" y2="1"><stop offset="0" stop-color="#8cbf2f"/><stop offset="1" stop-color="#c9e08a"/></linearGradient></defs><rect width="168" height="76" fill="#fff"/><path d="M0 0 L84 42 L168 0Z" fill="url(#flapGreen)"/><circle cx="84" cy="22" r="6" fill="#fff"/></svg>
</div>
<div class="envelope" style="top:24px">
  <svg width="168" height="76" viewBox="0 0 168 76"><defs><linearGradient id="flapOrange" x1="0" y1="0" x2="0" y2="1"><stop offset="0" stop-color="#e8801f"/><stop offset="1" stop-color="#f4b060"/></linearGradient></defs><rect width="168" height="76" fill="#fff"/><path d="M0 0 L84 42 L168 0Z" fill="url(#flapOrange)"/><circle cx="84" cy="22" r="6" fill="#3a4a14"/></svg>
</div>
<div class="label" style="left:728px;top:345px;width:168px">Envelope Set</div>

</body>
</html>
```